Business Card Design Can you design a business card design? Looking for something unique and differe

Can you design a business card design? Looking for something unique and different. Can you design a business card design? Looking for something unique and different.Can you design a business card design? Looking for something unique and different.Can you design a business card design? Looking for something unique and different.Can you design a business card design? Looking for something unique and different.Can you design a business card design? Looking for something unique and different.

Industry/Entity Type

Business

Contact Information for Business Card

Can you design a business card design? Looking for something unique and different.

Font styles to use
Serif

```html
<!DOCTYPE html>
<html lang="en">
<head>
<meta charset="utf-8">
<title>Remedium Business Card</title>
<link href="https://fonts.googleapis.com/css2?family=Lato:wght@400;700&display=swap" rel="stylesheet">
<style>
  :root {
    --paper: #e3e2e3;
    --band: #3e3e3e;
    --plum: #9c80ab;
    --plum-dark: #7d6489;
    --white: #ffffff;
  }
  html, body {
    margin: 0;
    padding: 0;
    width: 1200px;
    height: 720px;
    overflow: hidden;
    background: var(--paper);
  }
  .card {
    position: relative;
    width: 1200px;
    height: 720px;
    background: var(--paper);
    overflow: hidden;
  }
  .card__band {
    position: absolute;
    inset: 0;
    width: 1200px;
    height: 720px;
  }
  .brand-name {
    position: absolute;
    left: 0;
    right: 0;
    top: 318px;
    margin: 0;
    text-align: center;
    font-family: "Lato", sans-serif;
    font-weight: 700;
    font-size: 74px;
    letter-spacing: 1px;
    color: var(--plum);
  }
  .ribbon {
    position: absolute;
    left: 372px;
    top: 515px;
    width: 456px;
    height: 73px;
    background: var(--plum);
    border-radius: 0 0 6px 6px;
    display: flex;
    align-items: center;
    justify-content: center;
  }
  .ribbon__name {
    margin: 0;
    font-family: "Lato", sans-serif;
    font-weight: 400;
    font-size: 21px;
    color: var(--white);
  }
</style>
</head>
<body>
  <main class="card">
    <svg class="card__band" viewBox="0 0 1200 720" aria-hidden="true">
      <polygon fill="var(--band)" points="0,408 126,408 347,540 853,540 1072,408 1200,408 1200,720 0,720"/>
      <polygon fill="var(--plum-dark)" points="349,520 372,515 372,545"/>
      <polygon fill="var(--plum-dark)" points="851,520 828,515 828,545"/>
    </svg>
    <h1 class="brand-name">Remedium</h1>
    <div class="ribbon">
      <p class="ribbon__name">Dalton Mercer, Pharm. D President</p>
    </div>
  </main>
</body>
</html>
```